Design Emoji directory website with a modern look

Please design the Emoji directory website to display a nice search box as well as design a nice search suggestion dropdown page. Example when you type keyword in Brindlo.
You can use Emojis in SVG file https://www.filvex.com/s/8kq2207p5mzwtna/svg.rar?dl=0 to create designs.
The following are 7 example pages but please make sure the design is UNIQUE.
Main page example
https://glyphora.info/
Content page example
https://glyphora.info/smiling-face-with-smiling-eyes/
Category page example
https://glyphora.info/smileys-and-emotion-category/
Holiday page example
https://glyphora.info/holidays/
Static pages example
https://glyphora.info/privacy-policy/
404 page not found example
https://glyphora.info/category/
Search page example
https://glyphora.info/?s=exchange+rate
Target Market(s)
web design
Industry/Entity Type
Website
Number of Pages Required
5+ page
Font styles to use
Other font styles liked:
- COMIC NEUE
Colors
Designer to choose colors to be used in the design.
Requirements
Must have
- Please make sure its unique, modern look, clean.
Should not have
- Do not use heavy graphics, we only use CSS style rules and SVG's emojis to make sure the site loads fast.

```html
<!DOCTYPE html>
<html lang="en">
<head>
<meta charset="utf-8">
<title>Glyphnest – Emoji Directory</title>
<link rel="stylesheet" href="https://fonts.googleapis.com/css2?family=Poppins:wght@400;500;600;700;800&display=swap">
<style>
  :root {
    --purple: #5a2d8c;
    --purple-deep: #4a2377;
    --orange: #f5a623;
    --ink: #2b2b33;
    --muted: #8a8a95;
    --line: #e6e6ec;
    --card: #ffffff;
    --page: #ffffff;
    --footer: #2f2f35;
    --footer-text: #d8d8dd;
    --arrow-blue: #3d7fe0;
    --new-violet: #8a5ad8;
    --pager-blue: #39a3e6;
    --skin-1: #f7cf6b;
    --skin-2: #f1c9a5;
    --skin-3: #d9a57a;
    --skin-4: #a86d45;
    --skin-5: #6d4229;
  }
  * { box-sizing: border-box; margin: 0; padding: 0; }
  html, body { width: 1200px; height: 2400px; overflow: hidden; background: var(--page); }
  body { font-family: "Poppins", sans-serif; color: var(--ink); }
  .canvas { position: relative; width: 1200px; height: 2400px; overflow: hidden; }

  /* Hero */
  .hero { position: absolute; left: 0; top: 0; width: 1200px; height: 410px; background: var(--purple); }
  .brand { position: absolute; left: 140px; top: 60px; font-size: 62px; font-weight: 700; color: #fff; letter-spacing: -1px; }
  .hero-copy { position: absolute; left: 145px; top: 175px; width: 640px; font-size: 15px; line-height: 24px; color: #fff; }
  .search { position: absolute; left: 145px; top: 310px; width: 860px; height: 44px; background: #fff; border-radius: 22px; }
  .search-input { position: absolute; left: 26px; top: 12px; font-size: 14px; color: var(--muted); }
  .search-button { position: absolute; right: 0; top: 0; width: 120px; height: 44px; border-radius: 22px; background: var(--orange); color: #fff; font-size: 13px; font-weight: 700; display: flex; align-items: center; justify-content: center; gap: 6px; }
  .hero-art { position: absolute; border-radius: 14px; }
  .art-slot { left: 715px; top: 48px; width: 80px; height: 78px; background: #c9a6e8; border-radius: 12px; }
  .art-sparkle { left: 1085px; top: 40px; width: 40px; height: 40px; background: #7a52ad; border-radius: 50%; }
  .art-rider { left: 1035px; top: 290px; width: 165px; height: 200px; background: linear-gradient(160deg, #bfc6d3, #e55a5a 60%, #f5a623); border-radius: 30px 0 0 60px; }
  .art-shirt { left: 0; top: 380px; width: 150px; height: 150px; background: linear-gradient(150deg, #5fc4e8, #2b8fc7); border-radius: 0 40px 60px 0; }

  /* Cards */
  .card { position: absolute; width: 290px; background: var(--card); border-radius: 6px; box-shadow: 0 4px 16px rgba(40, 20, 70, .14); }
  .card-head { height: 52px; border-bottom: 1px solid var(--line); display: flex; align-items: center; gap: 12px; padding-left: 28px; font-size: 15px; font-weight: 600; }
  .checkbox { width: 15px; height: 15px; border: 2px solid var(--ink); border-radius: 3px; }
  .card-foot { position: absolute; left: 0; bottom: 0; width: 100%; height: 46px; border-top: 1px solid var(--line); display: flex; align-items: center; justify-content: center; font-size: 11px; font-weight: 500; color: var(--muted); letter-spacing: .5px; }
  .grid { display: grid; grid-template-columns: repeat(5, 34px); justify-content: space-between; padding: 24px 28px 0; row-gap: 22px; }
  .row-1 { top: 475px; height: 445px; }
  .row-2 { top: 940px; height: 480px; }
  .row-2 .grid { row-gap: 40px; padding-top: 30px; }
  .col-1 { left: 145px; } .col-2 { left: 455px; } .col-3 { left: 765px; }

  .flag { width: 34px; height: 24px; border-radius: 2px; margin: 5px 0; }
  .flag:nth-child(7n+1) { background: linear-gradient(#1f3a8a 50%, #d62a2a 50%); }
  .flag:nth-child(7n+2) { background: linear-gradient(90deg, #1e9e4a 33%, #fff 33% 66%, #d62a2a 66%); }
  .flag:nth-child(7n+3) { background: linear-gradient(#d62a2a 33%, #fff 33% 66%, #1e9e4a 66%); }
  .flag:nth-child(7n+4) { background: linear-gradient(#2a6ad6 33%, #f5c518 33% 66%, #2a6ad6 66%); }
  .flag:nth-child(7n+5) { background: linear-gradient(#111 33%, #d62a2a 33% 66%, #f5c518 66%); }
  .flag:nth-child(7n+6) { background: #1f3a8a; }
  .flag:nth-child(7n) { background: linear-gradient(90deg, #d62a2a 50%, #fff 50%); }

  .hand, .face { width: 30px; height: 30px; border-radius: 50%; margin: 2px auto; }
  .hand { border-radius: 45% 45% 40% 40%; }
  .hand:nth-child(5n+1), .face:nth-child(5n+1) { background: var(--skin-1); }
  .hand:nth-child(5n+2), .face:nth-child(5n+2) { background: var(--skin-2); }
  .hand:nth-child(5n+3), .face:nth-child(5n+3) { background: var(--skin-3); }
  .hand:nth-child(5n+4), .face:nth-child(5n+4) { background: var(--skin-4); }
  .hand:nth-child(5n), .face:nth-child(5n) { background: var(--skin-5); }

  .arrow { width: 30px; height: 30px; margin: 0 auto; border-radius: 4px; background: var(--arrow-blue); color: #fff; font-size: 18px; font-weight: 700; display: flex; align-items: center; justify-content: center; }
  .box-new { width: 30px; height: 30px; margin: 0 auto; border-radius: 4px; background: var(--new-violet); color: #fff; font-size: 15px; font-weight: 700; display: flex; align-items: center; justify-content: center; }
  .glyph { width: 34px; height: 34px; display: flex; align-items: center; justify-content: center; font-size: 26px; font-weight: 700; color: var(--ink); }
  .glyph.red { color: #e23b3b; } .glyph.green { color: #3bb54a; } .glyph.blue { color: var(--arrow-blue); } .glyph.violet { color: var(--new-violet); } .glyph.orange { color: var(--orange); }

  /* Pagination */
  .pager { position: absolute; left: 528px; top: 1490px; display: flex; gap: 6px; }
  .pager span { width: 20px; height: 20px; border: 1px solid var(--line); font-size: 10px; color: var(--muted); display: flex; align-items: center; justify-content: center; }
  .pager .current { background: var(--pager-blue); border-color: var(--pager-blue); color: #fff; }

  /* Testimonials */
  .section-title { position: absolute; left: 0; top: 1590px; width: 1200px; text-align: center; font-size: 42px; font-weight: 600; color: var(--ink); }
  .title-rule { position: absolute; left: 568px; top: 1668px; width: 64px; height: 3px; background: var(--orange); }
  .testimonial { position: absolute; left: 190px; top: 1740px; width: 820px; height: 280px; }
  .testimonial svg { position: absolute; left: 0; top: 0; }
  .quote-mark { position: absolute; left: 385px; top: 18px; font-size: 90px; line-height: 90px; font-weight: 800; color: #d9d9e0; }
  .quote-text { position: absolute; left: 120px; top: 110px; width: 580px; text-align: center; font-size: 11px; line-height: 18px; color: var(--muted); }
  .quote-author { position: absolute; left: 0; top: 200px; width: 820px; text-align: center; font-size: 18px; font-weight: 700; font-style: italic; }
  .stars { color: var(--orange); font-style: normal; font-size: 16px; margin-left: 6px; letter-spacing: 1px; }
  .nav-arrows { position: absolute; left: 560px; top: 2070px; display: flex; gap: 30px; }

  /* Footer */
  .footer { position: absolute; left: 0; top: 2180px; width: 1200px; height: 220px; background: var(--footer); color: var(--footer-text); }
  .footer-brand { position: absolute; left: 140px; top: 65px; font-size: 44px; font-weight: 700; color: #fff; letter-spacing: -1px; }
  .footer-info { position: absolute; top: 72px; display: flex; gap: 10px; font-size: 13px; line-height: 20px; }
  .footer-address { left: 410px; width: 230px; }
  .footer-phone { left: 690px; }
  .social { position: absolute; left: 940px; top: 76px; display: flex; gap: 14px; }
  .social span { width: 20px; height: 20px; border-radius: 50%; background: #fff; }
  .footer-rule { position: absolute; left: 140px; top: 160px; width: 920px; height: 1px; background: #45454c; }
  .copyright { position: absolute; left: 0; top: 176px; width: 1200px; text-align: center; font-size: 11px; color: #a9a9b0; }
  .top-link { position: absolute; right: 30px; top: 190px; font-size: 11px; color: #a9a9b0; }
</style>
</head>
<body>
<div class="canvas">

  <header class="hero">
    <div class="brand">Glyphnest</div>
    <p class="hero-copy">Lorem ipsum dolor sit amet, consectetur adipiscing elit, sed do eiusmod tempor incididunt ut labore et dolore magna aliqua. Quis ipsum suspendisse ultrices gravida.</p>
    <div class="search">
      <span class="search-input">Search Emojis..</span>
      <span class="search-button">
        <svg width="13" height="13" viewBox="0 0 14 14"><circle cx="6" cy="6" r="4.5" fill="none" stroke="#fff" stroke-width="2"/><line x1="9.5" y1="9.5" x2="13" y2="13" stroke="#fff" stroke-width="2"/></svg>
        SEARCH
      </span>
    </div>
    <div class="hero-art art-slot" role="img" aria-label="Slot machine emoji illustration"></div>
    <div class="hero-art art-sparkle" role="img" aria-label="Small sparkle emoji illustration"></div>
  </header>
  <div class="hero-art art-shirt" role="img" aria-label="Running shirt emoji illustration"></div>
  <div class="hero-art art-rider" role="img" aria-label="Snowboarder emoji illustration"></div>

  <section class="card row-1 col-1">
    <div class="card-head"><span class="checkbox"></span>Flags</div>
    <div class="grid">
      <span class="flag"></span><span class="flag"></span><span class="flag"></span><span class="flag"></span><span class="flag"></span>
      <span class="flag"></span><span class="flag"></span><span class="flag"></span><span class="flag"></span><span class="flag"></span>
      <span class="flag"></span><span class="flag"></span><span class="flag"></span><span class="flag"></span><span class="flag"></span>
      <span class="flag"></span><span class="flag"></span><span class="flag"></span><span class="flag"></span><span class="flag"></span>
      <span class="flag"></span><span class="flag"></span><span class="flag"></span><span class="flag"></span><span class="flag"></span>
      <span class="flag"></span><span class="flag"></span><span class="flag"></span><span class="flag"></span><span class="flag"></span>
    </div>
    <div class="card-foot">SEE ALL</div>
  </section>

  <section class="card row-1 col-2">
    <div class="card-head"><span class="checkbox"></span>Hands</div>
    <div class="grid">
      <span class="hand"></span><span class="hand"></span><span class="hand"></span><span class="hand"></span><span class="hand"></span>
      <span class="hand"></span><span class="hand"></span><span class="hand"></span><span class="hand"></span><span class="hand"></span>
      <span class="hand"></span><span class="hand"></span><span class="hand"></span><span class="hand"></span><span class="hand"></span>
      <span class="hand"></span><span class="hand"></span><span class="hand"></span><span class="hand"></span><span class="hand"></span>
      <span class="hand"></span><span class="hand"></span><span class="hand"></span><span class="hand"></span><span class="hand"></span>
      <span class="hand"></span><span class="hand"></span><span class="hand"></span><span class="hand"></span><span class="hand"></span>
    </div>
    <div class="card-foot">SEE ALL</div>
  </section>

  <section class="card row-1 col-3">
    <div class="card-head"><span class="checkbox"></span>Emojis</div>
    <div class="grid">
      <span class="face"></span><span class="face"></span><span class="face"></span><span class="face"></span><span class="face"></span>
      <span class="face"></span><span class="face"></span><span class="face"></span><span class="face"></span><span class="face"></span>
      <span class="face"></span><span class="face"></span><span class="face"></span><span class="face"></span><span class="face"></span>
      <span class="face"></span><span class="face"></span><span class="face"></span><span class="face"></span><span class="face"></span>
      <span class="face"></span><span class="face"></span><span class="face"></span><span class="face"></span><span class="face"></span>
      <span class="face"></span><span class="face"></span><span class="face"></span><span class="face"></span><span class="face"></span>
    </div>
    <div class="card-foot">SEE ALL</div>
  </section>

  <section class="card row-2 col-1">
    <div class="card-head"><span class="checkbox"></span>Direction Arrows</div>
    <div class="grid">
      <span class="arrow">↔</span><span class="arrow">↕</span><span class="arrow">↖</span><span class="arrow">↗</span><span class="arrow">↘</span>
      <span class="arrow">↙</span><span class="arrow">↩</span><span class="arrow">↪</span><span class="arrow">⤴</span><span class="arrow">⤵</span>
      <span class="arrow">⬆</span><span class="arrow">⬇</span><span class="arrow">⬅</span><span class="arrow">➡</span><span class="arrow">↻</span>
      <span class="arrow">▶</span><span class="arrow">◀</span><span class="arrow">⏫</span><span class="arrow">⏬</span><span class="arrow">⇄</span>
    </div>
    <div class="card-foot">SEE ALL</div>
  </section>

  <section class="card row-2 col-2">
    <div class="card-head"><span class="checkbox"></span>Somthing new</div>
    <div class="grid">
      <span class="box-new">♈</span><span class="box-new">♉</span><span class="box-new">♊</span><span class="box-new">♋</span><span class="box-new">♌</span>
      <span class="box-new">♍</span><span class="box-new">♎</span><span class="box-new">♏</span><span class="box-new">♐</span><span class="box-new">♑</span>
      <span class="box-new">♒</span><span class="box-new">♓</span><span class="box-new">⛎</span><span class="box-new">☮</span><span class="box-new">☯</span>
      <span class="box-new">✡</span><span class="box-new">☸</span><span class="box-new">⚛</span><span class="box-new">✴</span><span class="box-new">♾</span>
    </div>
    <div class="card-foot">SEE ALL</div>
  </section>

  <section class="card row-2 col-3">
    <div class="card-head"><span class="checkbox"></span>All Collections</div>
    <div class="grid">
      <span class="glyph">®</span><span class="glyph">©</span><span class="glyph">™</span><span class="glyph">‼</span><span class="glyph">⁉</span>
      <span class="glyph">−</span><span class="glyph red">!</span><span class="glyph red">♥</span><span class="glyph red">❗</span><span class="glyph">+</span>
      <span class="glyph green">✳</span><span class="glyph blue">❄</span><span class="glyph violet">✦</span><span class="glyph red">?</span><span class="glyph">?</span>
      <span class="glyph">✕</span><span class="glyph">✓</span><span class="glyph violet">◉</span><span class="glyph orange">✶</span><span class="glyph green">❇</span>
    </div>
    <div class="card-foot">SEE ALL</div>
  </section>

  <nav class="pager">
    <span class="current">1</span><span>2</span><span>3</span><span>4</span><span>»</span>
  </nav>

  <h2 class="section-title">Client Testimonials</h2>
  <div class="title-rule"></div>

  <section class="testimonial">
    <svg width="820" height="280" viewBox="0 0 820 280">
      <polygon points="150,4 670,4 816,140 670,276 150,276 4,140" fill="#fff" stroke="#ececf1" stroke-width="2"/>
    </svg>
    <div class="quote-mark">“</div>
    <p class="quote-text">Duis aute irure dolor in reprehenderit in voluptate velit esse cillum dolore eu fugiat nulla pariatur. Excepteur sint occaecat cupidatat non proident, sunt in culpa qui officia deserunt mollit anim id est laborum sed ut perspiciatis unde omnis iste natus.</p>
    <div class="quote-author">John Doe<span class="stars">★★★★★</span></div>
  </section>

  <div class="nav-arrows">
    <svg width="22" height="16" viewBox="0 0 22 16"><path d="M21 8H2M8 2L2 8l6 6" fill="none" stroke="#2b2b33" stroke-width="2"/></svg>
    <svg width="22" height="16" viewBox="0 0 22 16"><path d="M1 8h19M14 2l6 6-6 6" fill="none" stroke="#2b2b33" stroke-width="2"/></svg>
  </div>

  <footer class="footer">
    <div class="footer-brand">Glyphnest</div>
    <div class="footer-info footer-address">
      <svg width="12" height="16" viewBox="0 0 12 16"><path d="M6 0a6 6 0 0 0-6 6c0 4.5 6 10 6 10s6-5.5 6-10a6 6 0 0 0-6-6zm0 8.5A2.5 2.5 0 1 1 6 3.5a2.5 2.5 0 0 1 0 5z" fill="#fff"/></svg>
      <span>123,Lorem ipsum dolor sit amet consectetur adipiscing</span>
    </div>
    <div class="footer-info footer-phone">
      <svg width="14" height="14" viewBox="0 0 14 14"><path d="M3 0l2.5 3.5-1.6 1.6a8 8 0 0 0 5 5l1.6-1.6L14 11l-2 3C5.5 13.5.5 8.5 0 2z" fill="#fff"/></svg>
      <span>Phone : 1 800 555 0142</span>
    </div>
    <div class="social" aria-label="Social links"><span></span><span></span><span></span></div>
    <div class="footer-rule"></div>
    <p class="copyright">© 2020 Glyphnest . All Rights reserved | Privacy Policy | Terms and Use</p>
    <span class="top-link">Up</span>
  </footer>

</div>
</body>
</html>
```